RW Framewell Inc Business cards

We need business cards using our existing logo but slightly modified. Right now the logo says RW Bedrock Masonry. We want to keep the RW part of the design, but replace the Bedrock Masonry portion with "FRAMEWELL". Please see the attached file.
Ideally this would be a blank template so we can add Different Names, titles, and phone numbers later.
On the one side we want only the logo and on the other side the detail. I'm attaching an example for you to see.
Please reach out with any other questions. Our address and other details will be given out once we find a design we like.

Target Market(s)

Construction Industry

```html
<!DOCTYPE html>
<html lang="en">
<head>
<meta charset="utf-8">
<title>RW Framewell Inc Business Cards</title>
<link href="https://fonts.googleapis.com/css2?family=Michroma&family=Open+Sans:wght@400&display=swap" rel="stylesheet">
<style>
  :root {
    --stage: #2a2a2a;
    --brand-blue: #1279c1;
    --brand-blue-light: #2a8ad2;
    --brand-gray: #7d7d7d;
    --paper: #ffffff;
  }
  html, body {
    margin: 0;
    width: 1200px;
    height: 900px;
    overflow: hidden;
    background: var(--stage);
  }
  .canvas {
    position: relative;
    width: 1200px;
    height: 900px;
  }
  .card {
    position: absolute;
    left: 267px;
    width: 665px;
    height: 380px;
    overflow: hidden;
    box-shadow: 0 10px 30px rgba(0,0,0,.55);
  }
  .card--back { top: 48px; background: var(--brand-blue); }
  .card--front { top: 468px; background: var(--paper); }

  .back-texture {
    position: absolute;
    inset: 0;
    background: linear-gradient(135deg, var(--brand-blue-light), var(--brand-blue) 60%);
  }
  .back-wordmark {
    position: absolute;
    inset: 0;
    display: flex;
    align-items: center;
    justify-content: center;
    gap: 14px;
    font-family: "Michroma", sans-serif;
    color: var(--paper);
    font-size: 34px;
    letter-spacing: 1px;
  }
  .back-wordmark .mark-square {
    width: 18px; height: 18px; background: var(--paper);
  }

  .front-wordmark {
    position: absolute;
    left: 34px;
    top: 34px;
    display: flex;
    align-items: center;
    gap: 12px;
    font-family: "Michroma", sans-serif;
    font-size: 32px;
    color: var(--brand-blue);
    letter-spacing: 1px;
  }
  .front-wordmark .mark-square {
    width: 16px; height: 16px; background: var(--brand-blue);
  }
  .person {
    position: absolute;
    left: 40px;
    top: 104px;
  }
  .person-name {
    font-family: "Michroma", sans-serif;
    font-size: 24px;
    line-height: 34px;
    color: var(--brand-blue);
    letter-spacing: 1px;
    margin: 0;
  }
  .person-title {
    font-family: "Open Sans", sans-serif;
    font-size: 17px;
    line-height: 24px;
    color: var(--brand-gray);
    margin: 0;
  }
  .contact-band {
    position: absolute;
    left: 0;
    top: 176px;
    width: 665px;
    height: 168px;
    background: var(--brand-blue);
  }
  .contact {
    position: absolute;
    left: 40px;
    top: 186px;
    margin: 0;
    padding: 0;
    list-style: none;
    font-family: "Open Sans", sans-serif;
    font-size: 17px;
    line-height: 24px;
    color: var(--paper);
  }
  .contact li { display: flex; align-items: center; gap: 10px; }
  .contact .icon { width: 16px; height: 16px; flex: none; }
  .contact .address { margin-top: 4px; }
</style>
</head>
<body>
<main class="canvas">

  <section class="card card--back" aria-label="Card back">
    <div class="back-texture" role="img" aria-label="Faint repeated monogram texture in lighter blue"></div>
    <div class="back-wordmark">
      <span class="mark-square"></span>
      <span>RW FRAMEWELL</span>
    </div>
  </section>

  <section class="card card--front" aria-label="Card front">
    <div class="contact-band" role="img" aria-label="Blue brand band behind the contact details"></div>

    <div class="front-wordmark">
      <span class="mark-square"></span>
      <span>RW FRAMEWELL</span>
    </div>

    <div class="person">
      <p class="person-name">DANA MERCER</p>
      <p class="person-title">Chief Officer</p>
    </div>

    <ul class="contact">
      <li>
        <svg class="icon" viewBox="0 0 16 16"><path d="M3 1 L6 1 L7 5 L5 6.5 Q6.5 9.5 9.5 11 L11 9 L15 10 L15 13 Q15 15 13 15 Q2 14 1 3 Q1 1 3 1Z" fill="#fff"/></svg>
        <span>+00 8 38 00 00</span>
      </li>
      <li>
        <svg class="icon" viewBox="0 0 16 16"><rect x="4" y="1" width="8" height="14" rx="1.5" fill="none" stroke="#fff" stroke-width="1.6"/><circle cx="8" cy="12.5" r="0.9" fill="#fff"/></svg>
        <span>+00 0 90 00 00</span>
      </li>
      <li>
        <svg class="icon" viewBox="0 0 16 16"><rect x="1" y="3.5" width="14" height="9" fill="none" stroke="#fff" stroke-width="1.5"/><path d="M1 3.5 L8 9 L15 3.5" fill="none" stroke="#fff" stroke-width="1.5"/></svg>
        <span>info@rwframewell.com</span>
      </li>
      <li>
        <svg class="icon" viewBox="0 0 16 16"><circle cx="8" cy="8" r="6.5" fill="none" stroke="#fff" stroke-width="1.4"/><ellipse cx="8" cy="8" rx="3" ry="6.5" fill="none" stroke="#fff" stroke-width="1.2"/><path d="M1.5 8 H14.5" stroke="#fff" stroke-width="1.2"/></svg>
        <span>www.rwframewell.com</span>
      </li>
      <li class="address">Your address line here</li>
      <li>Country/ State</li>
    </ul>
  </section>

</main>
</body>
</html>
```